Flyer für freiberuflichen Bauingenieur
Zielgruppe
Ich bin freiberuflicher Bauingenieur und erstelle vermehrt Schadstoffkataster für zum Abbruch vorgesehene Gebäude im Auftrag von Abbruchunternehmen und Eigentümern.
Aufgabenstellung
Ich habe die Rahmenbedingungen in eine Worddatei geschrieben, auch vorgesehenes Format Farben etc.

```html
<!DOCTYPE html>
<html lang="de">
<head>
<meta charset="utf-8">
<title>Flyer Bauplanungs- und Ingenieurbüro</title>
<link rel="stylesheet" href="https://fonts.googleapis.com/css2?family=Open+Sans:wght@400;700;800&family=Montserrat:wght@400;500;600&family=Roboto+Condensed:wght@700&family=Kalam:wght@400&display=swap">
<style>
  :root{
    --navy:#0c5580;
    --navy-deep:#0a4a70;
    --paper:#ecebe9;
    --paper-line:#d8d8d6;
    --green:#6e9a1c;
    --white:#ffffff;
    --ink:#1d1d1d;
    --ghost:#d4d4d2;
    --stone-a:#8f8a83;
    --stone-b:#b9b4ad;
    --tick-red:#c8102e;
    --stage:#e6e5ea;
  }
  *{box-sizing:border-box;margin:0;padding:0}
  html,body{width:1200px;height:800px;overflow:hidden;background:var(--stage)}
  .stage{position:relative;width:1200px;height:800px}
  .page{position:absolute;top:146px;width:360px;height:508px;background:var(--paper);overflow:hidden;box-shadow:0 2px 8px rgba(0,0,0,.18)}
  .page--front{left:198px}
  .page--back{left:632px}
  .page svg.bg{position:absolute;inset:0}
  .band-green{position:absolute;left:0;right:0;bottom:0;height:10px;background:var(--green)}

  /* front */
  .brand{position:absolute;left:18px;top:14px;width:326px;color:var(--white)}
  .brand__name{font-family:"Open Sans",sans-serif;font-weight:800;font-size:18.5px;letter-spacing:.9px;padding-bottom:4px;border-bottom:1px solid #8fb0c4}
  .brand__sub{font-family:"Open Sans",sans-serif;font-weight:400;font-size:14.3px;letter-spacing:.6px;margin-top:6px}
  .ghost{position:absolute;font-family:"Roboto Condensed",sans-serif;font-weight:700;color:var(--ghost);line-height:1;white-space:nowrap}
  .script{position:absolute;font-family:"Kalam",cursive;color:var(--navy);font-size:33px;line-height:1}

  /* back */
  .intro{position:absolute;left:13px;top:7px;width:336px;color:var(--white);font-family:"Montserrat",sans-serif}
  .intro__head{font-weight:500;font-size:9.4px;line-height:12px;text-transform:uppercase;padding-bottom:3px;border-bottom:1px solid var(--green)}
  .intro__list{list-style:none;margin-top:3px}
  .intro__list li{position:relative;padding-left:11px;font-size:9.6px;line-height:15px}
  .intro__list li::before{content:"·";position:absolute;left:1px;top:0}
  .checks{position:absolute;left:20px;top:170px}
  .check{position:relative;height:31px}
  .check__bar{position:absolute;left:17px;top:2px;width:114px;height:20px;background:var(--navy);clip-path:polygon(0 0,100% 0,100% 100%,4% 100%);display:flex;align-items:center;padding-left:13px;font-family:"Open Sans",sans-serif;font-weight:700;color:var(--white);font-size:15px}
  .check__bar--small{font-size:10.5px}
  .check svg{position:absolute;left:0;top:0}
  .office{position:absolute;width:160px;font-family:"Montserrat",sans-serif;color:var(--ink)}
  .office__title{background:var(--navy);color:var(--white);font-weight:600;font-size:7.4px;height:12px;line-height:12px;padding-left:5px}
  .office__line{font-size:7.2px;line-height:11.4px;padding-left:5px}
</style>
</head>
<body>
<main class="stage">

  <section class="page page--front">
    <svg class="bg" width="360" height="508" viewBox="0 0 360 508">
      <polygon points="0,0 360,0 360,94 0,357" fill="var(--navy)"/>
    </svg>

    <span class="ghost" style="left:318px;top:185px;font-size:46px;writing-mode:vertical-rl">ASBEST</span>
    <span class="ghost" style="left:290px;top:215px;font-size:22px;writing-mode:vertical-rl">FORMALDEHYD</span>
    <span class="ghost" style="left:195px;top:270px;font-size:52px">PAK</span>
    <span class="ghost" style="left:205px;top:330px;font-size:34px">DDT</span>
    <span class="ghost" style="left:150px;top:365px;font-size:60px">PCP</span>
    <span class="ghost" style="left:180px;top:430px;font-size:20px">KMF/ WHO-/</span>
    <span class="ghost" style="left:175px;top:452px;font-size:20px">LUNGENGÄNGIGE</span>
    <span class="ghost" style="left:220px;top:474px;font-size:20px">FASERN</span>
    <span class="ghost" style="left:20px;top:400px;font-size:62px">PAK</span>
    <span class="ghost" style="left:4px;top:370px;font-size:15px;writing-mode:vertical-rl">FORMALDEHYD</span>

    <svg class="bg" width="360" height="508" viewBox="0 0 360 508">
      <defs>
        <linearGradient id="stoneTone" x1="0" y1="0" x2="1" y2="1">
          <stop offset="0" stop-color="var(--stone-b)"/>
          <stop offset="1" stop-color="var(--stone-a)"/>
        </linearGradient>
      </defs>
      <ellipse cx="120" cy="402" rx="110" ry="12" fill="#000" opacity=".12"/>
      <path role="img" aria-label="Foto eines schwebenden grauen Gesteinsbrockens mit Schadstoffprobe" d="M55,78 L85,72 L118,98 L150,150 L185,215 L225,300 L230,350 L190,392 L110,398 L45,380 L24,330 L30,260 L18,200 L34,130 Z" fill="url(#stoneTone)"/>
      <polygon role="img" aria-label="Beispielseite eines Untersuchungsberichts mit Probenfotos und Laborbefunden" points="216,67 351,148 216,358 72,268" fill="#f6f6f4" stroke="#cfcfcd" stroke-width="1"/>
    </svg>

    <header class="brand">
      <div class="brand__name">DIPL.-ING. TOBIAS WENNING</div>
      <div class="brand__sub">BAUPLANUNGS- UND INGENIEURBÜRO</div>
    </header>

    <span class="script" style="left:34px;top:402px">Planung, Bauleitung</span>
    <span class="script" style="left:38px;top:448px">und mehr ...</span>

    <div class="band-green"></div>
  </section>

  <section class="page page--back">
    <svg class="bg" width="360" height="508" viewBox="0 0 360 508">
      <rect role="img" aria-label="Hintergrund mit blassen Bauplänen und technischen Zeichnungen" x="0" y="0" width="360" height="508" fill="var(--paper)"/>
      <polygon points="0,0 360,0 360,76 270,154 0,142" fill="var(--navy)"/>
      <circle role="img" aria-label="Foto eines teilweise abgerissenen Fachwerkhauses hinter einem Bauzaun" cx="235" cy="256" r="108" fill="#7c7563"/>
    </svg>

    <div class="intro">
      <p class="intro__head">Durchführung von Gebäudeuntersuchung mit Probenentnahme, Laboranalyse und Auswertung über Untersuchungsbericht/Schadstoffkataster zur:</p>
      <ul class="intro__list">
        <li>Ermittlung von notwendigen Vorarbeiten (vorgeschalteter Rückbau Asbest/Gefahrstoffe)</li>
        <li>Vorbereitung der Planung der Arbeiten und des Arbeitsschutzes</li>
        <li>gezielten Angebotserstellung für Auftraggeber</li>
        <li>Zur Vorlage bei Deponien, als Nachweis der Belastung/Belastungsfreiheit</li>
      </ul>
    </div>

    <div class="checks">
      <div class="check"><svg width="24" height="24" viewBox="0 0 24 24"><circle cx="12" cy="12" r="10" fill="#fff" stroke="var(--green)" stroke-width="2"/><path d="M7 11.5 L11 16.5 L17 6" fill="none" stroke="var(--tick-red)" stroke-width="2.4" stroke-linecap="round"/></svg><div class="check__bar">ASBEST</div></div>
      <div class="check"><svg width="24" height="24" viewBox="0 0 24 24"><circle cx="12" cy="12" r="10" fill="#fff" stroke="var(--green)" stroke-width="2"/><path d="M7 11.5 L11 16.5 L17 6" fill="none" stroke="var(--tick-red)" stroke-width="2.4" stroke-linecap="round"/></svg><div class="check__bar">PAK</div></div>
      <div class="check"><svg width="24" height="24" viewBox="0 0 24 24"><circle cx="12" cy="12" r="10" fill="#fff" stroke="var(--green)" stroke-width="2"/><path d="M7 11.5 L11 16.5 L17 6" fill="none" stroke="var(--tick-red)" stroke-width="2.4" stroke-linecap="round"/></svg><div class="check__bar">PCB</div></div>
      <div class="check"><svg width="24" height="24" viewBox="0 0 24 24"><circle cx="12" cy="12" r="10" fill="#fff" stroke="var(--green)" stroke-width="2"/><path d="M7 11.5 L11 16.5 L17 6" fill="none" stroke="var(--tick-red)" stroke-width="2.4" stroke-linecap="round"/></svg><div class="check__bar">DDT</div></div>
      <div class="check"><svg width="24" height="24" viewBox="0 0 24 24"><circle cx="12" cy="12" r="10" fill="#fff" stroke="var(--green)" stroke-width="2"/><path d="M7 11.5 L11 16.5 L17 6" fill="none" stroke="var(--tick-red)" stroke-width="2.4" stroke-linecap="round"/></svg><div class="check__bar check__bar--small">FORMALDEHYD</div></div>
      <div class="check"><svg width="24" height="24" viewBox="0 0 24 24"><circle cx="12" cy="12" r="10" fill="#fff" stroke="var(--green)" stroke-width="2"/><path d="M7 11.5 L11 16.5 L17 6" fill="none" stroke="var(--tick-red)" stroke-width="2.4" stroke-linecap="round"/></svg><div class="check__bar">PCP</div></div>
    </div>

    <div class="office" style="left:19px;top:370px">
      <div class="office__title">Nordhain (Hauptsitz)</div>
      <div class="office__line">Lindenhofweg 14</div>
      <div class="office__line">29999 Nordhain</div>
      <div class="office__line">Telefon. +49 (0) 50 00 / 1 23 45</div>
      <div class="office__line">Mobil. +49 (0) 150 /00 11 22 33</div>
    </div>
    <div class="office" style="left:193px;top:370px">
      <div class="office__title">Büro Heidmoor</div>
      <div class="office__line">Am Kirchberg 8</div>
      <div class="office__line">21999 Brunstedt</div>
      <div class="office__line">Telefon. +49 (0) 40 00 / 98 76 543</div>
      <div class="office__line">Mobil. +49 (0) 150 /00 11 22 33</div>
    </div>
    <div class="office" style="left:19px;top:432px">
      <div class="office__title">Büro Ostfelde</div>
      <div class="office__line">Wiesengrund 5</div>
      <div class="office__line">23999 Ostfelde</div>
      <div class="office__line">Telefon. (Festnetz folgt)</div>
      <div class="office__line">Mobil. +49 (0) 150 /00 11 22 33</div>
    </div>
    <div class="office" style="left:193px;top:432px">
      <div class="office__title">Büro Talbeck am Forst</div>
    </div>

    <div class="band-green"></div>
  </section>

</main>
</body>
</html>
```